A new presentation to our clients

we are a Real Estate agency, our website is www.dorelumia.com and it’s time to have a new, fashion and remarcable Business Card. we want to differentiate ourselves from other companies so we want a business card that differentiates us. we want the business card to impact our customers. in the competitive market that we have today, we have to be different and it is this difference that we seek

Target Market(s)

Real Estate Clients

Contact Information for Business Card

We search a totaly diferent card from the usual

Font styles to use
Sans Serif

Colors
e34197

Requirements
Must have
• Logo, adress, phone contact, e-mail, photo, and our website
Nice to have
• We would like to see a modern business card
Should not have
• Houses or building draws

```html
<!DOCTYPE html>
<html lang="pt">
<head>
<meta charset="utf-8">
<title>Dore Lumia – Business Card</title>
<link href="https://fonts.googleapis.com/css2?family=Jost:wght@300;400;500&display=swap" rel="stylesheet">
<style>
  :root {
    --brand-pink: #e34197;
    --ink: #3a3a3a;
    --muted: #8d8d8d;
    --card: #ffffff;
    --backdrop: #d9d9d9;
    --rule: #111111;
  }
  * { margin: 0; padding: 0; box-sizing: border-box; }
  html, body {
    width: 1200px;
    height: 960px;
    overflow: hidden;
    background: var(--backdrop);
    font-family: "Jost", "Helvetica Neue", Arial, sans-serif;
  }
  .stage {
    width: 1200px;
    height: 960px;
    display: flex;
    align-items: center;
    justify-content: center;
  }
  .business-card {
    position: relative;
    width: 1000px;
    height: 572px;
    background: var(--card);
    box-shadow: 0 10px 30px rgba(0,0,0,0.18);
    overflow: hidden;
  }
  .brand-name {
    position: absolute;
    left: 440px;
    top: 120px;
    font-size: 76px;
    font-weight: 500;
    color: var(--brand-pink);
    line-height: 1;
  }
  .person {
    position: absolute;
    left: 140px;
    top: 255px;
  }
  .person-name {
    font-size: 46px;
    font-weight: 400;
    color: var(--brand-pink);
    letter-spacing: -1px;
    line-height: 1;
  }
  .person-role {
    font-size: 26px;
    font-weight: 300;
    color: var(--muted);
    margin-top: 4px;
    margin-left: 30px;
    line-height: 1;
  }
  .contact-list {
    list-style: none;
    margin-top: 20px;
    margin-left: 60px;
    font-size: 23px;
    font-weight: 400;
    color: var(--ink);
    line-height: 1.6;
  }
  .contact-label { color: var(--brand-pink); font-weight: 500; margin-right: 8px; }
  .contact-gap { display: inline-block; width: 16px; }
  .address {
    position: absolute;
    right: 90px;
    top: 462px;
    font-size: 23px;
    font-weight: 400;
    color: var(--ink);
    line-height: 1;
    white-space: nowrap;
  }
  .address-rule {
    position: absolute;
    left: 0;
    width: 720px;
    top: 500px;
    height: 1.5px;
    background: var(--rule);
  }
  .website {
    position: absolute;
    right: 30px;
    top: 512px;
    font-size: 23px;
    font-weight: 400;
    color: var(--brand-pink);
    line-height: 1;
  }
</style>
</head>
<body>
  <main class="stage">
    <section class="business-card" aria-label="Dore Lumia business card">
      <div class="brand-name">Dore Lumia</div>

      <div class="person">
        <div class="person-name">MARTA LEAL</div>
        <div class="person-role">CEO/FOUNDER</div>
        <ul class="contact-list">
          <li><span class="contact-label">P :</span>(+351) 220 418 140<span class="contact-gap"></span><span class="contact-label">F :</span>(+351) 220 418 149</li>
          <li><span class="contact-label">E :</span>geral@dorelumia.com</li>
        </ul>
      </div>

      <div class="address">Av. das Camélias, 58, 4400-236 , Vila Nova de Gaia</div>
      <div class="address-rule"></div>
      <div class="website">www.dorelumia.com</div>
    </section>
  </main>
</body>
</html>
```